Targeted Marketing

Postcard will be sent to customers who’ve already been contacted or will be in the next week or two reiterating information found on my website www.pinevaleminerals.example. Trying to keep my company name in the forefront of their mind when it comes time to divest their mineral interests.

```html
<!DOCTYPE html>
<html lang="en">
<head>
<meta charset="utf-8">
<title>Pinevale Minerals – Postcard Back</title>
<link href="https://fonts.googleapis.com/css2?family=Open+Sans:wght@300;400&display=swap" rel="stylesheet">
<style>
  :root {
    --brand-red: #e8232a;
    --ink: #111111;
    --rule: #555555;
    --paper: #ffffff;
    --edge: #000000;
  }
  html, body {
    margin: 0;
    padding: 0;
    overflow: hidden;
    background: var(--paper);
  }
  .postcard {
    position: relative;
    width: 1200px;
    height: 816px;
    background: var(--paper);
    overflow: hidden;
    font-family: "Open Sans", Arial, sans-serif;
  }
  .edge-bar {
    position: absolute;
    left: 0;
    top: 0;
    width: 48px;
    height: 768px;
    background: var(--edge);
  }
  .footer-band {
    position: absolute;
    left: 48px;
    top: 768px;
    width: 1152px;
    height: 48px;
    background: var(--brand-red);
  }
  .brand {
    position: absolute;
    left: 56px;
    top: 66px;
    display: flex;
    align-items: center;
    gap: 12px;
  }
  .brand-mark {
    width: 26px;
    height: 26px;
    background: var(--brand-red);
  }
  .brand-name {
    font-weight: 400;
    font-size: 34px;
    letter-spacing: 0.01em;
    color: var(--brand-red);
    line-height: 1;
  }
  .divider {
    position: absolute;
    left: 600px;
    top: 128px;
    width: 1px;
    height: 579px;
    background: var(--rule);
  }
  .stamp-box {
    position: absolute;
    left: 1013px;
    top: 48px;
    width: 138px;
    height: 170px;
    border: 1px solid #333333;
  }
  .address-lines {
    position: absolute;
    left: 672px;
    top: 484px;
    width: 410px;
  }
  .address-line {
    height: 1px;
    background: #777777;
    margin-bottom: 49px;
  }
  .contact {
    position: absolute;
    left: 62px;
    top: 530px;
    margin: 0;
    font-style: normal;
    font-weight: 300;
    font-size: 29px;
    line-height: 32px;
    letter-spacing: 0.09em;
    color: var(--brand-red);
  }
  .contact span { display: block; white-space: nowrap; }
  .contact .contact-email { color: var(--ink); letter-spacing: 0.07em; }
</style>
</head>
<body>
  <main class="postcard">
    <div class="edge-bar"></div>

    <div class="brand">
      <div class="brand-mark"></div>
      <div class="brand-name">Pinevale Minerals</div>
    </div>

    <div class="divider"></div>
    <div class="stamp-box"></div>

    <div class="address-lines">
      <div class="address-line"></div>
      <div class="address-line"></div>
      <div class="address-line"></div>
      <div class="address-line"></div>
    </div>

    <address class="contact">
      <span>Contact Us</span>
      <span>Pinevale Minerals LLC</span>
      <span>Attn: Colby R. Marsh</span>
      <span>PO Box 4410</span>
      <span>Roswell, NM 88203</span>
      <span>555.703.0146</span>
      <span class="contact-email">colby@pinevaleminerals.example</span>
    </address>

    <div class="footer-band"></div>
  </main>
</body>
</html>
```